Pedicure Menu with 8 Scent Options

This design will be for a single page menu (front/back) that will display multiple different scent variations of a product. The purpose of this menu is to display to clients and show them the available options and benefits of each option.
The menu will be double sided.
The front page will include a header including brand logo and product name, and a total of 8 different scents including imagery and descriptive text.
The design should include the text provided for each scent. The design should have a layout that is structured/organized, easy to read, and has bright imagery that represents each scent.
An example is a modular layout using boxes that highlight a different scent within each box. Lavender scent should include aesthetic images of lavender flower and/or the color purple.
The back page will include brand logo, overall product description, and additional brief text that explains each step of the product.
The final size of the design should be 8.5"x11", produced in InDesign format, with all layers editable for future changes.
NOTE: Please carefully review the attached design brief that includes additional information, and all necessary text to include in the design.
Target Market(s)
Beauty/Spa Clients
Industry/Entity Type
Beauty
Requirements
Must have
- Bright and Vivid Imagery/Illustrations
Nice to have
- Background design that utilizes, lines, shapes, or other elements.

```html
<!DOCTYPE html>
<html lang="en">
<head>
<meta charset="utf-8">
<title>Deluxe Pedicure 4-Step Menu</title>
<link href="https://fonts.googleapis.com/css2?family=Allura&family=Roboto:wght@400;700&family=Roboto+Condensed:wght@400;700&display=swap" rel="stylesheet">
<style>
:root{
  --stage:#334536;
  --paper:#f7efe8;
  --ink:#2e4230;
  --gold:#c49a5a;
  --footer:#231f20;
  --text:#2a2a2a;
}
*{margin:0;padding:0;box-sizing:border-box}
html,body{width:1200px;height:834px;overflow:hidden;background:var(--stage)}
.page{position:absolute;top:101px;width:488px;height:632px;background:radial-gradient(circle at 15% 10%,#fbf7f3 0,var(--paper) 45%,#f4e9df 100%);overflow:hidden;font-family:"Roboto Condensed",sans-serif;color:var(--text)}
.page--front{left:98px}
.page--back{left:619px;height:635px}
.masthead{position:absolute;left:0;right:0;top:18px;text-align:center}
.masthead__script{font-family:"Allura",cursive;font-size:56px;line-height:1;color:var(--gold);display:block;height:44px}
.masthead__title{font-family:"Roboto",sans-serif;font-weight:700;font-size:29px;color:var(--ink);line-height:1;letter-spacing:.3px;margin-top:-4px}
.masthead__sub{font-family:"Roboto",sans-serif;font-size:12px;letter-spacing:4px;color:#222;margin-top:4px}
.scent{position:absolute;width:214px;height:104px;background:#fff;border:1px solid #5a5a5a}
.scent__image{position:absolute;left:5px;top:6px;width:64px;height:90px;border-radius:6px}
.scent__name{position:absolute;left:74px;top:10px;font-family:"Allura",cursive;font-size:24px;line-height:1;white-space:nowrap;font-weight:400}
.scent__name--long{font-size:20px;top:12px}
.scent__desc{position:absolute;left:74px;top:39px;width:136px;height:43px;border:1px solid;padding:3px 3px;font-size:6.6px;line-height:1.3;text-align:justify;color:#222;overflow:hidden}
.footer{position:absolute;left:0;right:0;bottom:0;height:56px;background:var(--footer);color:#fff;padding:8px 25px 0}
.footer__claims{font-size:12px;letter-spacing:.2px}
.footer__claims span{color:var(--gold)}
.footer__note{font-size:7.3px;margin-top:6px;color:#eee}
.footer__brand{position:absolute;right:28px;top:12px;font-family:"Roboto Condensed",sans-serif;font-size:22px;font-weight:400;color:#fff;display:flex;align-items:center;gap:5px}
.footer__brand i{width:6px;height:6px;border-radius:50%;background:#fff;display:block}
.intro{position:absolute;left:40px;right:40px;top:135px;text-align:center;font-size:9.2px;line-height:1.3;color:#222}
.step{position:absolute;width:195px}
.step__photo{width:195px;height:150px;border:1px solid #6b6b6b}
.step__title{font-family:"Roboto Condensed",sans-serif;font-weight:700;font-size:17px;color:var(--ink);margin-top:4px;line-height:1;white-space:nowrap}
.step__text{font-size:9.5px;margin-top:1px;color:#222;white-space:nowrap}
</style>
</head>
<body>

<section class="page page--front">
  <header class="masthead">
    <span class="masthead__script">Deluxe</span>
    <h1 class="masthead__title">PEDICURE 4-STEP</h1>
    <p class="masthead__sub">PICK YOUR PEDICURE</p>
  </header>

  <article class="scent" style="left:25px;top:120px">
    <div class="scent__image" role="img" aria-label="Lavender sprigs" style="background:linear-gradient(160deg,#8e6cc0,#6a4d9c 60%,#7a9a5a)"></div>
    <h2 class="scent__name" style="color:#a98bc9">Lavender</h2>
    <p class="scent__desc" style="border-color:#c5aedf">Lorem ipsum dolor sit amet, consectetur adipiscing elit, sed do eiusmod tempor ididunt ut labore et dolore magna aliqua. Ut enim ad minim veniam.</p>
  </article>
  <article class="scent" style="left:264px;top:120px">
    <div class="scent__image" role="img" aria-label="Fresh mint leaves" style="background:radial-gradient(circle,#6fb054,#3e8a3a 70%,#fff 72%)"></div>
    <h2 class="scent__name" style="color:#6fdbc5">Mint</h2>
    <p class="scent__desc" style="border-color:#9fe6d6">Lorem ipsum dolor sit amet, consectetur adipiscing elit, sed do eiusmod tempor ididunt ut labore et dolore magna aliqua. Ut enim ad minim veniam.</p>
  </article>
  <article class="scent" style="left:25px;top:235px">
    <div class="scent__image" role="img" aria-label="Mandarin oranges" style="background:radial-gradient(circle,#f9a531,#ef7e16 60%,#fff 72%)"></div>
    <h2 class="scent__name" style="color:#e85a2a">Mandarin</h2>
    <p class="scent__desc" style="border-color:#f3b562">Lorem ipsum dolor sit amet, consectetur adipiscing elit, sed do eiusmod tempor ididunt ut labore et dolore magna aliqua. Ut enim ad minim veniam.</p>
  </article>
  <article class="scent" style="left:264px;top:235px">
    <div class="scent__image" role="img" aria-label="Red roses" style="background:radial-gradient(circle,#d0202a,#9c1018 60%,#fff 72%)"></div>
    <h2 class="scent__name" style="color:#d8262f">Rose</h2>
    <p class="scent__desc" style="border-color:#d8262f">Lorem ipsum dolor sit amet, consectetur adipiscing elit, sed do eiusmod tempor ididunt ut labore et dolore magna aliqua. Ut enim ad minim veniam.</p>
  </article>
  <article class="scent" style="left:25px;top:350px">
    <div class="scent__image" role="img" aria-label="White jasmine flowers" style="background:radial-gradient(circle,#fff 30%,#ece9e2 60%,#fff 75%)"></div>
    <h2 class="scent__name" style="color:#e8c55a">Jasmine</h2>
    <p class="scent__desc" style="border-color:#eed98f">Lorem ipsum dolor sit amet, consectetur adipiscing elit, sed do eiusmod tempor ididunt ut labore et dolore magna aliqua. Ut enim ad minim veniam.</p>
  </article>
  <article class="scent" style="left:264px;top:350px">
    <div class="scent__image" role="img" aria-label="Glass of milk with honeycomb" style="background:linear-gradient(90deg,#f1f1ef 55%,#f0b93a 56%,#e3a52a)"></div>
    <h2 class="scent__name" style="color:var(--gold)">Milk &amp; Honey</h2>
    <p class="scent__desc" style="border-color:#d3b574">Lorem ipsum dolor sit amet, consectetur adipiscing elit, sed do eiusmod tempor ididunt ut labore et dolore magna aliqua. Ut enim ad minim veniam.</p>
  </article>
  <article class="scent" style="left:25px;top:465px">
    <div class="scent__image" role="img" aria-label="Watermelon slices and cucumbers" style="background:linear-gradient(180deg,#e0463a 45%,#5f9c3e 55%,#a9cf7a)"></div>
    <h2 class="scent__name scent__name--long" style="color:#3f7a3d">Cucumber-Melon</h2>
    <p class="scent__desc" style="border-color:#8fbc6a">Lorem ipsum dolor sit amet, consectetur adipiscing elit, sed do eiusmod tempor ididunt ut labore et dolore magna aliqua. Ut enim ad minim veniam.</p>
  </article>
  <article class="scent" style="left:264px;top:465px">
    <div class="scent__image" role="img" aria-label="Green tea leaves" style="background:radial-gradient(ellipse at 50% 65%,#3a4a2a,#5f8a3a 50%,#fff 72%)"></div>
    <h2 class="scent__name" style="color:#3f7a3d">Green-Tea</h2>
    <p class="scent__desc" style="border-color:#9cc46a">Lorem ipsum dolor sit amet, consectetur adipiscing elit, sed do eiusmod tempor ididunt ut labore et dolore magna aliqua. Ut enim ad minim veniam.</p>
  </article>

  <footer class="footer">
    <p class="footer__claims">PARABEN <span>FREE</span> &nbsp;•&nbsp; GLUTEN <span>FREE</span> &nbsp;•&nbsp; CURLITY <span>FREE</span></p>
    <p class="footer__note">lorem ispum lorem lorem ispum lorem lorem ispum lorem lorem lorem ispum lorem</p>
    <div class="footer__brand"><i></i>Velora</div>
  </footer>
</section>

<section class="page page--back">
  <header class="masthead">
    <span class="masthead__script">Deluxe</span>
    <h1 class="masthead__title">PEDICURE 4-STEP</h1>
    <p class="masthead__sub">PICK YOUR PEDICURE</p>
  </header>

  <p class="intro">Velora Deluxe Pedicure 4-Step will transform your pedicure experience and immerse your senses into a floral paradise designed to rejuvenate your body. Sit back, relax, and enjoy.</p>

  <div class="step" style="left:37px;top:174px">
    <div class="step__photo" role="img" aria-label="Hands rubbing salt onto a foot" style="background:linear-gradient(135deg,#f4dccd,#e7b79e 50%,#f3e6df)"></div>
    <h2 class="step__title">1. Salt Soak</h2>
    <p class="step__text">Detoxifies and deodorizes your feet.</p>
  </div>
  <div class="step" style="left:261px;top:174px">
    <div class="step__photo" role="img" aria-label="Sugar scrub applied to a foot" style="background:linear-gradient(160deg,#f8f4ee,#ecc6a8 55%,#d9b69a)"></div>
    <h2 class="step__title">2. Sugar Scrub</h2>
    <p class="step__text">Gently exfoliates dead skin.</p>
  </div>
  <div class="step" style="left:37px;top:377px">
    <div class="step__photo" role="img" aria-label="Masque brushed onto a foot beside candles" style="background:linear-gradient(160deg,#4a3a30,#c89e86 45%,#8e8a66 70%,#2d4a70)"></div>
    <h2 class="step__title">3. Foot Masque</h2>
    <p class="step__text">Cleanses pores for smoother skin.</p>
  </div>
  <div class="step" style="left:261px;top:377px">
    <div class="step__photo" role="img" aria-label="Hands massaging a foot with lotion" style="background:linear-gradient(150deg,#f3ede6,#eac2a8 55%,#f6f1ec)"></div>
    <h2 class="step__title">4. Massage Lotion</h2>
    <p class="step__text">Hydrates and soothes skin.</p>
  </div>

  <footer class="footer">
    <p class="footer__claims">PARABEN <span>FREE</span> &nbsp;•&nbsp; GLUTEN <span>FREE</span> &nbsp;•&nbsp; CURLITY <span>FREE</span></p>
    <p class="footer__note">lorem ispum lorem lorem ispum lorem lorem ispum lorem lorem lorem ispum lorem</p>
    <div class="footer__brand"><i></i>Velora</div>
  </footer>
</section>

</body>
</html>
```